Business Card for Orvane Parts Wholesale supplier

Hi There! I need a new business card for our company. We are specialized in selling Orvane parts, mostly we sell new LCD screens for Telvox and Slatrons. I would like to see that back in the design.

You can find the colors and logo's on our website: www.dorvak-example.nl

Industry/Entity Type

Business

Contact Information for Business Card

My Details:
Lars Vintorp

Phone: 0031612873406
E-mail: Lars@dorvak-example.nl

Slogan: "Because Quality Matters"

Font styles to use
Sans Serif

Colors

Designer to choose colors to be used in the design.

Requirements
Must have
• A Black backside with the Dorvak logo on it. The front side should be clean with only my contact details.
• But I'm also open for something really different or awesome!
Nice to have
• Remember that we are in the parts & repairing industry, So i'll be handing those business cards mainly to repair companies. Maybe you can do something with that thought :)

```html
<!DOCTYPE html>
<html lang="en">
<head>
<meta charset="utf-8">
<title>Dorvak Business Card</title>
<link href="https://fonts.googleapis.com/css2?family=Michroma&family=Roboto:wght@400&display=swap" rel="stylesheet">
<style>
  :root {
    --stage: #e6e4e1;
    --card-front: #ffffff;
    --card-back: #2b2b2b;
    --ink: #111111;
    --muted: #555555;
    --accent: #f26a21;
    --rule: #8a8a8a;
    --light: #f2f2f2;
  }
  html, body {
    margin: 0;
    padding: 0;
    width: 1200px;
    height: 1200px;
    overflow: hidden;
    background: var(--stage);
  }
  .canvas {
    position: relative;
    width: 1200px;
    height: 1200px;
  }
  .card {
    position: absolute;
    left: 214px;
    width: 772px;
    height: 440px;
    box-shadow: 0 3px 10px rgba(0,0,0,0.18);
  }
  .card--front { top: 150px; background: var(--card-front); }
  .card--back  { top: 633px; background: var(--card-back); }

  .brand {
    position: absolute;
    display: flex;
    align-items: center;
  }
  .brand__mark {
    background: var(--accent);
    border-radius: 6px;
    flex: none;
  }
  .brand__name {
    font-family: "Michroma", sans-serif;
    font-weight: 400;
    letter-spacing: 1px;
    line-height: 1;
  }
  .card--front .brand { left: 58px; top: 185px; gap: 14px; }
  .card--front .brand__mark { width: 60px; height: 60px; }
  .card--front .brand__name { font-size: 38px; color: var(--ink); }

  .divider {
    position: absolute;
    left: 392px;
    top: 150px;
    width: 1px;
    height: 139px;
    background: var(--rule);
  }
  .contact {
    position: absolute;
    left: 428px;
    top: 145px;
  }
  .contact__name {
    margin: 0 0 24px;
    font-family: "Michroma", sans-serif;
    font-size: 23px;
    font-weight: 400;
    letter-spacing: 2px;
    color: var(--ink);
  }
  .contact__list {
    list-style: none;
    margin: 0;
    padding: 0;
    font-family: "Roboto", sans-serif;
    font-size: 18.5px;
    color: var(--muted);
  }
  .contact__item {
    display: flex;
    align-items: center;
    gap: 8px;
    height: 27.5px;
  }
  .contact__icon { width: 16px; height: 16px; flex: none; }

  .card--back .brand {
    left: 0; right: 0; top: 165px;
    justify-content: center;
    gap: 26px;
  }
  .card--back .brand__mark { width: 110px; height: 110px; border-radius: 10px; }
  .card--back .brand__name { font-size: 64px; color: var(--light); }
  .back-url {
    position: absolute;
    left: 0; right: 0; top: 384px;
    text-align: center;
    font-family: "Roboto", sans-serif;
    font-size: 19.5px;
    color: var(--light);
  }
</style>
</head>
<body>
<main class="canvas">
  <section class="card card--front" aria-label="Business card front">
    <div class="brand">
      <span class="brand__mark"></span>
      <span class="brand__name">dorvak</span>
    </div>
    <div class="divider"></div>
    <div class="contact">
      <h1 class="contact__name">LARS VINTORP</h1>
      <ul class="contact__list">
        <li class="contact__item">
          <svg class="contact__icon" viewBox="0 0 16 16" fill="none" stroke="#f26a21" stroke-width="1.2"><path d="M3 1.5l2.5 0 1 3.5-1.6 1.2a8 8 0 0 0 4.9 4.9l1.2-1.6 3.5 1v2.5c0 .8-.7 1.5-1.5 1.5A12.5 12.5 0 0 1 1.5 3c0-.8.7-1.5 1.5-1.5z"/></svg>
          <span>0031612873406</span>
        </li>
        <li class="contact__item">
          <svg class="contact__icon" viewBox="0 0 16 16" fill="none" stroke="#f26a21" stroke-width="1.2"><rect x="1" y="3" width="14" height="10"/><path d="M1 3l7 6 7-6"/></svg>
          <span>Lars@dorvak-example.nl</span>
        </li>
        <li class="contact__item">
          <svg class="contact__icon" viewBox="0 0 16 16" fill="none" stroke="#f26a21" stroke-width="1.2"><circle cx="8" cy="8" r="6.5"/><ellipse cx="8" cy="8" rx="3" ry="6.5"/><path d="M1.5 8h13M2.5 4.5h11M2.5 11.5h11"/></svg>
          <span>www.dorvak-example.nl</span>
        </li>
      </ul>
    </div>
  </section>

  <section class="card card--back" aria-label="Business card back">
    <div class="brand">
      <span class="brand__mark"></span>
      <span class="brand__name">dorvak</span>
    </div>
    <p class="back-url">www.dorvak-sample.example</p>
  </section>
</main>
</body>
</html>
```